IV Nutritional Therapy Website Design

We are working with an IV Therapy company in California. They provide iv hydration services throughout California.

Some sites to use for inspiration:
https://www.lumavelterra.com
https://corvantique.com
https://tessimorclinic.com (I love this option matrix. We need a nice way to present this on the homepage)
https://ambervalenix.com

Thank you for taking the time to consider designing a website for us. We are web developers based in Stockton, CA, USA. Most of our projects go through the same process. Understanding this process may help you win a project with us. We custom-code all of our websites in-house. We don’t have any requirements as to what tools you use for your design, but we ask that you follow these guidelines.

IMAGES:
If you use any images or icons in the design, we ask that you have a link to the asset so we can purchase the image/icon. Most of the designs we submit do not have the customer’s images on them unless they have some great images. Be creative; show us the feeling you are trying to portray with your image choices. Use any royalty-free site you choose. We subscribe to Adobe and mainly use their images, but we can purchase images outside of Adobe. PLEASE NOTE: we will not submit designs to clients with watermarks on the images.

FONTS:
We ask that you identify the fonts you’re using in the design. This can be done in a message if you want. We typically use Google Fonts and Adobe Fonts.

CONTENT:
We're always open to different content and ideas. We often submit designs with stock images so the client can see our vision. We typically take pictures after the website launch to use their images with our vision. Lorem Ipsum is fine for paragraphs, but we ask that you make the Headers with correct English. We want to be able to show the vision and identify the sections of the website.

INSPIRATION:
We typically add a couple of links in the brief of websites we like to help you get started in your design.

REVISIONS:
We do not often ask for revisions of the designs unless we see something in the design that may not appeal to the client. If there are slight changes that we want to make, we do that in the development process.

FEEDBACK:
We rarely give feedback on designs during the design process. We are working on many website projects and do not have the time to provide feedback. We usually respond if your request is well thought out and asks specific questions, but a note asking “feedback, please” usually goes unanswered.

```html
<!DOCTYPE html>
<html lang="en">
<head>
<meta charset="utf-8">
<title>Novaire Hydration — IV Hydration Across California</title>
<link href="https://fonts.googleapis.com/css2?family=Mulish:wght@400;500;600;700;800;900&display=swap" rel="stylesheet">
<style>
:root{
  --navy:#1a2a85;
  --navy-dark:#1c2267;
  --green:#77a23b;
  --ink:#333a4d;
  --muted:#555b6b;
  --row:#f4f6ec;
  --line:#c9cbe0;
  --mist:#f1f0f1;
  --white:#ffffff;
}
*{box-sizing:border-box;margin:0;padding:0}
html,body{width:1200px;height:4666px;overflow:hidden}
body{font-family:"Mulish",Arial,sans-serif;color:var(--ink);background:var(--white);position:relative}
.section{position:absolute;left:0;width:1200px}
.btn{display:inline-flex;align-items:center;justify-content:center;background:var(--green);color:var(--white);font-weight:800;font-size:12px;letter-spacing:.3px;text-transform:uppercase;text-decoration:none}
.btn-navy{background:var(--navy)}
.title{font-weight:800;color:var(--navy);font-size:23px;text-align:center;text-transform:uppercase;letter-spacing:.2px}
.underline{width:58px;height:3px;background:var(--green);margin:18px auto 0}
.underline.light{background:var(--white)}

/* Header */
.site-header{top:0;height:100px}
.brand{position:absolute;left:130px;top:26px;font-weight:900;font-size:34px;color:var(--navy);letter-spacing:1px}
.main-nav{position:absolute;left:340px;top:38px;display:flex;gap:0}
.main-nav a{font-size:13px;font-weight:600;color:#222;text-decoration:none;margin-right:30px;position:relative;letter-spacing:.2px}
.main-nav a.active{color:var(--green)}
.main-nav a.active::after{content:"";position:absolute;left:0;right:0;top:24px;height:2px;background:var(--green)}
.site-header .btn{position:absolute;left:923px;top:28px;width:148px;height:38px;font-size:13px;font-weight:700}

/* Hero */
.hero{top:100px;height:555px}
.hero-photo{position:absolute;inset:0;background:linear-gradient(90deg,#7d7f78 0%,#b9bdb7 30%,#d8dcdc 55%,#e9ecee 75%,#c9cdd2 100%)}
.hero h1{position:absolute;left:132px;top:88px;width:420px;color:var(--white);font-size:37px;line-height:42px;font-weight:800}
.hero .btn{position:absolute;left:137px;top:320px;width:168px;height:44px;font-size:13px}
.dots{position:absolute;left:570px;top:511px;display:flex;gap:12px}
.dots span{width:11px;height:11px;border-radius:50%;background:var(--white)}
.dots span.on{background:var(--navy)}

/* Benefits */
.benefits{top:655px;height:695px}
.benefits .title{margin-top:52px}
.benefit-grid{position:absolute;left:132px;top:150px;width:938px;display:grid;grid-template-columns:1fr 1fr 1fr;row-gap:40px}
.benefit{text-align:center;padding:0 12px}
.benefit-icon{width:62px;height:56px;margin:0 auto;border-radius:50%;background:radial-gradient(circle,#dfe9cd 0 45%,transparent 46%)}
.benefit h3{font-size:15px;font-weight:700;color:var(--navy);margin-top:16px}
.benefit p{font-size:12px;line-height:19px;color:var(--muted);margin:14px auto 0;width:222px}
.v-rule{position:absolute;top:155px;width:1px;height:402px;background:#9aa0b8}
.benefits .btn{position:absolute;left:491px;top:607px;width:217px;height:36px;font-size:11px}

/* Welcome / pricing */
.welcome{top:1350px;height:612px;background:var(--navy);color:var(--white)}
.welcome .title{color:var(--white);margin-top:48px}
.welcome .lead{width:780px;margin:28px auto 0;text-align:center;font-size:14.5px;line-height:23px}
.plans{position:absolute;left:132px;top:218px;display:flex;gap:36px}
.plan{width:288px;height:342px;background:var(--white);text-align:center;color:var(--ink);position:relative;padding-top:28px}
.plan .badge{position:absolute;top:-10px;left:50%;transform:translateX(-50%);background:var(--green);color:var(--white);font-size:11px;font-weight:800;padding:2px 5px}
.plan h3{color:var(--navy);font-size:18px;font-weight:700}
.plan .sub{font-size:13px;color:var(--muted);margin-top:7px}
.plan .price{color:var(--green);font-size:38px;font-weight:800;margin-top:16px;line-height:44px}
.plan .labs{font-size:13px;color:var(--muted)}
.plan p{font-size:12px;line-height:19px;color:var(--muted);width:220px;margin:20px auto 0}
.plan .btn{width:130px;height:35px;font-size:11px;margin-top:20px}
.plan .btn-navy{margin-top:9px}

/* Plan overview table */
.overview{top:1962px;height:943px}
.overview .title{margin-top:40px}
.matrix{position:absolute;left:132px;top:118px;width:938px;box-shadow:0 8px 18px rgba(0,0,0,.06);padding-bottom:10px}
.matrix .row{display:grid;grid-template-columns:430px 154px 146px 192px;column-gap:5px;height:32px;align-items:center;font-size:11.5px;color:var(--ink)}
.matrix .row:nth-child(odd):not(.head) > span{background:var(--row)}
.matrix .row > span{height:30px;display:flex;align-items:center;justify-content:center}
.matrix .row > span:first-child{justify-content:flex-start;padding-left:34px}
.matrix .head{height:34px;margin-bottom:6px}
.matrix .head > span{background:var(--navy);color:var(--white);height:34px;font-size:12px}
.matrix .head > span:first-child{padding:0}
.matrix svg{width:18px;height:18px}
.matrix .fee{font-size:11.5px}

/* Nutritional therapy */
.nutrition{top:2905px;height:440px;background:var(--mist)}
.nutrition-photo{position:absolute;left:580px;top:0;width:620px;height:440px;background:radial-gradient(ellipse at 60% 45%,#dfe0e2 0%,#cfd2d6 35%,#e9e8ea 70%,var(--mist) 100%)}
.nutrition h2{position:absolute;left:134px;top:58px;font-size:23px;font-weight:800;color:var(--navy)}
.nutrition .bar{position:absolute;left:134px;top:99px;width:58px;height:3px;background:var(--green)}
.nutrition p{position:absolute;left:134px;top:130px;width:410px;font-size:13.5px;line-height:23px;color:var(--ink)}
.nutrition .btn{position:absolute;left:136px;top:345px;width:107px;height:36px;font-size:11px}

/* Service cards */
.services{top:3345px;height:620px}
.service{position:absolute;top:63px;width:450px;height:498px;border:1.5px solid #8e93bd;text-align:center;padding-top:40px}
.service-icon{width:90px;height:94px;margin:0 auto;border-radius:8px;background:radial-gradient(circle,#e0eacf 0 48%,transparent 49%)}
.service h3{color:var(--navy);font-size:20px;font-weight:800;line-height:32px;margin-top:30px;text-transform:uppercase}
.service p{font-size:13.5px;line-height:21px;color:var(--muted);width:346px;margin:24px auto 0}
.service .btn{width:222px;height:36px;font-size:11px;margin-top:30px}

/* CTA */
.cta{top:3965px;height:505px}
.cta-photo{position:absolute;inset:0;background:linear-gradient(90deg,#a8b0c2 0%,#c9cfdb 20%,#8c8fa8 40%,#c9b7c4 60%,#d8cdb8 80%,#b3aec0 100%)}
.cta h2{position:absolute;left:557px;top:112px;font-size:39px;line-height:54px;font-weight:900;color:var(--navy);text-transform:uppercase}
.cta h2 span{background:rgba(255,255,255,.85);padding:0 10px;box-decoration-break:clone;-webkit-box-decoration-break:clone}
.cta .btn{position:absolute;left:560px;top:275px;width:206px;height:44px;font-size:14px}

/* Footer */
.site-footer{top:4470px;height:196px;background:var(--navy-dark);color:var(--white)}
.site-footer .brand{left:136px;top:40px;color:var(--white);font-size:32px}
.follow{position:absolute;left:872px;top:47px;display:flex;align-items:center;gap:18px;font-size:12px;font-weight:700}
.follow i{width:15px;height:15px;border-radius:50%;background:var(--white);display:inline-block}
.footer-nav{position:absolute;left:512px;top:84px;display:flex;gap:30px}
.footer-nav a{color:var(--white);text-decoration:none;font-size:12.5px;font-weight:600}
.footer-rule{position:absolute;left:132px;top:120px;width:938px;height:1px;background:rgba(255,255,255,.45)}
.copyright{position:absolute;top:157px;width:100%;text-align:center;font-size:11.5px;color:#d5d8ec}
</style>
</head>
<body>

<header class="section site-header">
  <div class="brand">NOVAIRE</div>
  <nav class="main-nav">
    <a class="active" href="#">HOME</a>
    <a href="#">ABOUT US</a>
    <a href="#">IV NUTRITIONAL THERAPY</a>
    <a href="#">TREATMENTS</a>
    <a href="#">CONTACT US</a>
  </nav>
  <a class="btn" href="#">SCHEDULE A VISIT</a>
</header>

<section class="section hero">
  <div class="hero-photo" role="img" aria-label="Man in a white t-shirt drinking water while receiving an IV drip in a bright room"></div>
  <h1>Revitalize Your Wellness with Premium IV Hydration Services Across California</h1>
  <a class="btn" href="#">SCHEDULE A VISIT</a>
  <div class="dots"><span></span><span class="on"></span><span></span></div>
</section>

<section class="section benefits">
  <h2 class="title">Benefits of IV Drip Therapy</h2>
  <div class="underline"></div>
  <div class="v-rule" style="left:425px"></div>
  <div class="v-rule" style="left:790px"></div>
  <div class="benefit-grid">
    <div class="benefit"><div class="benefit-icon" role="img" aria-label="Hydration icon"></div><h3>Hydration</h3><p>Lorem ipsum dolor sit amet, conse ctetur adipiscing elit, sed do eiusmod tempor incididunt ut labore et dolore magna aliqua Ut enim.</p></div>
    <div class="benefit"><div class="benefit-icon" role="img" aria-label="Immune defense icon"></div><h3>Immune Defense</h3><p>Lorem ipsum dolor sit amet, conse ctetur adipiscing elit, sed do eiusmod tempor incididunt ut labore et dolore magna aliqua Ut enim.</p></div>
    <div class="benefit"><div class="benefit-icon" role="img" aria-label="Increase energy icon"></div><h3>Increase Energy</h3><p>Lorem ipsum dolor sit amet, conse ctetur adipiscing elit, sed do eiusmod tempor incididunt ut labore et dolore magna aliqua Ut enim.</p></div>
    <div class="benefit"><div class="benefit-icon" role="img" aria-label="Anti-aging icon"></div><h3>Anti-aging Effects</h3><p>Lorem ipsum dolor sit amet, conse ctetur adipiscing elit, sed do eiusmod tempor incididunt ut labore et dolore magna aliqua Ut enim.</p></div>
    <div class="benefit"><div class="benefit-icon" role="img" aria-label="Mental clarity icon"></div><h3>Mental Clarity</h3><p>Lorem ipsum dolor sit amet, conse ctetur adipiscing elit, sed do eiusmod tempor incididunt ut labore et dolore magna aliqua Ut enim.</p></div>
    <div class="benefit"><div class="benefit-icon" role="img" aria-label="Hangover recovery icon"></div><h3>Hangover Recovery</h3><p>Lorem ipsum dolor sit amet, conse ctetur adipiscing elit, sed do eiusmod tempor incididunt ut labore et dolore magna aliqua Ut enim.</p></div>
  </div>
  <a class="btn" href="#">LEARN MORE ABOUT IV DRIPS</a>
</section>

<section class="section welcome">
  <h2 class="title">Welcome to Novaire Hydration</h2>
  <div class="underline light"></div>
  <p class="lead">Sed ut perspiciatis unde omnis iste natus error sit voluptatem accusantium doloremque laudantium totam rem aperiam, eaque ipsa quae ab illo inventore veritatis et quasi architecto beatae vitae</p>
  <div class="plans">
    <div class="plan">
      <h3>Hormone Focus</h3><div class="sub">Regulating Hormone Levels</div>
      <div class="price">$365</div><div class="labs">plus labs</div>
      <p>Lorem ipsum dolor sit amet, conse ctetur adipiscing elit, sed do</p>
      <a class="btn" href="#">GET STARTED</a><br><a class="btn btn-navy" href="#">MORE INFO</a>
    </div>
    <div class="plan">
      <span class="badge">MOST POPULAR</span>
      <h3>Overall Health</h3><div class="sub">Health Treatment Summary</div>
      <div class="price">$900</div><div class="labs">plus labs</div>
      <p>Lorem ipsum dolor sit amet, conse ctetur adipiscing elit, sed do</p>
      <a class="btn" href="#">GET STARTED</a><br><a class="btn btn-navy" href="#">MORE INFO</a>
    </div>
    <div class="plan">
      <h3>Comprehensive Health</h3><div class="sub">Detailed Personalized Treatment</div>
      <div class="price">$2135</div><div class="labs">plus labs</div>
      <p>Lorem ipsum dolor sit amet, conse ctetur adipiscing elit, sed do</p>
      <a class="btn" href="#">GET STARTED</a><br><a class="btn btn-navy" href="#">MORE INFO</a>
    </div>
  </div>
</section>

<section class="section overview">
  <svg width="0" height="0" style="position:absolute">
    <defs>
      <symbol id="tick" viewBox="0 0 20 20"><polyline points="3,10.5 8,15 17,4.5" fill="none" stroke="#77a23b" stroke-width="2.4" stroke-linecap="round" stroke-linejoin="round"/></symbol>
      <symbol id="cross" viewBox="0 0 20 20"><path d="M4 4L16 16M16 4L4 16" stroke="#1a2a85" stroke-width="2" stroke-linecap="round"/></symbol>
    </defs>
  </svg>
  <h2 class="title">Plan Overview</h2>
  <div class="underline"></div>
  <div class="matrix">
    <div class="row head"><span></span><span>Hormone Focus</span><span>Overall Health</span><span>Comprehensive Health</span></div>
    <div class="row"><span>Hormone Levels</span><span><svg><use href="#tick"/></svg></span><span><svg><use href="#tick"/></svg></span><span><svg><use href="#tick"/></svg></span></div>
    <div class="row"><span>PSA (for men)</span><span><svg><use href="#tick"/></svg></span><span><svg><use href="#tick"/></svg></span><span><svg><use href="#tick"/></svg></span></div>
    <div class="row"><span>Blood Count</span><span><svg><use href="#tick"/></svg></span><span><svg><use href="#tick"/></svg></span><span><svg><use href="#tick"/></svg></span></div>
    <div class="row"><span>Heart Risk Assessment</span><span></span><span></span><span></span></div>
    <div class="row"><span>Diabetes Risk Assessment</span><span></span><span></span><span></span></div>
    <div class="row"><span>Thyroid Risk Assessment</span><span></span><span></span><span></span></div>
    <div class="row"><span>Liver Assessment</span><span><svg><use href="#cross"/></svg></span><span><svg><use href="#tick"/></svg></span><span><svg><use href="#tick"/></svg></span></div>
    <div class="row"><span>Kidney Assessment</span><span><svg><use href="#cross"/></svg></span><span><svg><use href="#tick"/></svg></span><span><svg><use href="#tick"/></svg></span></div>
    <div class="row"><span>Vitamin B12</span><span><svg><use href="#cross"/></svg></span><span><svg><use href="#tick"/></svg></span><span><svg><use href="#tick"/></svg></span></div>
    <div class="row"><span>Vitamin D</span><span><svg><use href="#cross"/></svg></span><span><svg><use href="#tick"/></svg></span><span><svg><use href="#tick"/></svg></span></div>
    <div class="row"><span>Magnesium</span><span><svg><use href="#cross"/></svg></span><span><svg><use href="#tick"/></svg></span><span><svg><use href="#tick"/></svg></span></div>
    <div class="row"><span>Iron</span><span><svg><use href="#cross"/></svg></span><span><svg><use href="#tick"/></svg></span><span><svg><use href="#tick"/></svg></span></div>
    <div class="row"><span>Blood Chemistry Panel</span><span><svg><use href="#cross"/></svg></span><span><svg><use href="#tick"/></svg></span><span><svg><use href="#tick"/></svg></span></div>
    <div class="row"><span>Inflammation</span><span><svg><use href="#cross"/></svg></span><span><svg><use href="#tick"/></svg></span><span><svg><use href="#tick"/></svg></span></div>
    <div class="row"><span>Growth Hormone</span><span><svg><use href="#cross"/></svg></span><span><svg><use href="#tick"/></svg></span><span><svg><use href="#tick"/></svg></span></div>
    <div class="row"><span>Autoimmune Screen</span><span><svg><use href="#cross"/></svg></span><span><svg><use href="#tick"/></svg></span><span><svg><use href="#tick"/></svg></span></div>
    <div class="row"><span>Tumor Markers</span><span><svg><use href="#cross"/></svg></span><span><svg><use href="#tick"/></svg></span><span><svg><use href="#tick"/></svg></span></div>
    <div class="row"><span>Orvanta Multi-Cancer Early Detection Test</span><span><svg><use href="#cross"/></svg></span><span><svg><use href="#tick"/></svg></span><span><svg><use href="#tick"/></svg></span></div>
    <div class="row fee"><span>First Visit Fees</span><span>$195</span><span>$450</span><span>$1,575</span></div>
    <div class="row fee"><span>Lab Fees</span><span>$0-$121</span><span>$0-$376</span><span>$0-$855</span></div>
    <div class="row fee"><span>Second Visit Fees</span><span>$85 male, $170 female</span><span>$450</span><span>$560</span></div>
    <div class="row fee"><span>Subsequent Visits</span><span>$85-$170</span><span>$85-$170</span><span>$85-$170</span></div>
  </div>
</section>

<section class="section nutrition">
  <div class="nutrition-photo" role="img" aria-label="IV drip bag and tubing with a syringe on a light background"></div>
  <h2>IV NUTRITIONAL THERAPY</h2>
  <div class="bar"></div>
  <p>Sed ut perspiciatis unde omnis iste natus error sit voluptatem accusantium doloremque laudantium, totam rem aperiam, eaque ipsa quae ab illo inventore veritatis et quasi architecto beatae vitae dicta sunt explicabo. Nemo enim ipsam voluptatem quia voluptas sit aspernatur aut odit aut fugit, sed quia consequuntur magni dolores eos qui ratione voluptatem sequi nesciunt. Neque porro quisquam est, qui dolorem ipsum quia dolor sit ame</p>
  <a class="btn" href="#">READ MORE</a>
</section>

<section class="section services">
  <div class="service" style="left:132px">
    <div class="service-icon" role="img" aria-label="Hormone molecule icon"></div>
    <h3>Bio-Identical Hormone<br>Restoration</h3>
    <p>Sed ut perspiciatis unde omnis iste natus error sit voluptatem accusantium doloremque laudantium, totam rem aperiam, eaque ipsa quae ab illo inve ntore veritatis et quasi architecto beatae vitae dicta sunt explicabo. Nemo enim ipsam voluptatem quia voluptas sit aspernatur aut odit aut fugit sed quia consequuntur</p>
    <a class="btn" href="#">REQUEST YOUR CONSULTATION</a>
  </div>
  <div class="service" style="left:620px">
    <div class="service-icon" role="img" aria-label="Knee joint injection icon"></div>
    <h3>Regenerative Joint<br>Injections</h3>
    <p>Sed ut perspiciatis unde omnis iste natus error sit voluptatem accusantium doloremque laudantium, totam rem aperiam, eaque ipsa quae ab illo inve ntore veritatis et quasi architecto beatae vitae dicta sunt explicabo. Nemo enim ipsam voluptatem quia voluptas sit aspernatur aut odit aut fugit sed quia consequuntur</p>
    <a class="btn" href="#">REQUEST YOUR CONSULTATION</a>
  </div>
</section>

<section class="section cta">
  <div class="cta-photo" role="img" aria-label="IV bag hanging on a stand in front of a softly blurred clinic background"></div>
  <h2><span>Are you ready to</span><br><span>live your best life?</span></h2>
  <a class="btn" href="#">GET STARTED TODAY</a>
</section>

<footer class="section site-footer">
  <div class="brand">NOVAIRE</div>
  <div class="follow">FOLLOW US <i></i><i></i><i></i></div>
  <nav class="footer-nav">
    <a href="#">HOME</a><a href="#">ABOUT US</a><a href="#">IV NUTRITIONAL THERAPY</a><a href="#">TREATMENTS</a><a href="#">CONTACT US</a>
  </nav>
  <div class="footer-rule"></div>
  <div class="copyright">Copyright © 2023 All Rights Reserved</div>
</footer>

</body>
</html>
```